New DermaLune logo and packaging

We would like a new design for our new product DermaLune, a high strength vitamin C serum which treats pigmentation. The packaging will reflect a high quality, clinical product with the logo "DermaLune" on the front, with it's ingredients "Vitamin C, B3, B5, E and ferulic acid" the products are in two sizes 10ml and 30ml.

This is one of many products to come out in the DermaLune range.

It would be for high end medical clinics selling premium brands, with a strong medical and clinical feel, professional and current or even futuristic in appearance.

Gold, blue, silver, White, cream are all colours that do this (without appearing cheap)

The product is not tested on animals, so would have
- "Not tested on animals".
- "12m" symbol for shelf life,
- "Made in USA"
- and ingredients list

See attached the product and existing box

Target Market(s)

Medical and aesthetic clinics

Font styles to use
Serif
Sans Serif

Colors
33a6d7
cee9f5
ffffff
fbed22
fee18a

Requirements
Must have
• High end premium brand
Nice to have
• like the idea of gold and silver lettering on cream background
Should not have
• Tacky, over complicated design

```html
<!DOCTYPE html>
<html lang="en">
<head>
<meta charset="utf-8">
<title>DermaLune Vitamin C Serum – Carton Front</title>
<link rel="stylesheet" href="https://fonts.googleapis.com/css2?family=Cabin+Condensed:wght@400;500&family=Lato:wght@400&display=swap">
<style>
  :root {
    --backdrop: #9a9a9a;
    --carton: #d9d8e0;
    --carton-light: #e4e3ea;
    --panel-blue: #1f73b8;
    --panel-text: #e6e6ee;
    --ink: #2a2a2a;
    --brand-blue: #1f73b8;
    --gold-dark: #8a4a12;
    --gold-mid: #c8792a;
    --gold-light: #f6d58a;
  }
  * { box-sizing: border-box; margin: 0; padding: 0; }
  html, body { width: 942px; height: 1200px; overflow: hidden; }
  body { background: var(--backdrop); position: relative; font-family: "Lato", sans-serif; }

  .carton-front {
    position: absolute; left: 339px; top: 221px; width: 264px; height: 756px;
    background: linear-gradient(90deg, var(--carton) 0%, var(--carton-light) 50%, var(--carton) 100%);
  }

  .gold-rule {
    position: absolute; height: 5px;
    background: linear-gradient(90deg, var(--gold-dark), var(--gold-mid) 20%, var(--gold-light) 45%, var(--gold-mid) 70%, var(--gold-dark));
  }

  .title-panel {
    position: absolute; left: 0; top: 109px; width: 220px; height: 327px;
    background: var(--panel-blue); color: var(--panel-text);
    font-family: "Cabin Condensed", sans-serif; text-align: center;
  }
  .title-panel .gold-rule { left: 0; width: 100%; }
  .title-panel .gold-rule.top { top: 0; }
  .title-panel .gold-rule.bottom { bottom: 0; }
  .title-word { position: absolute; left: 0; width: 100%; line-height: 1; }
  .title-vitamin { top: 36px; font-size: 46px; font-weight: 400; }
  .title-letter { top: 92px; font-size: 104px; font-weight: 500; }
  .title-serum { top: 202px; font-size: 44px; font-weight: 400; }
  .title-divider { position: absolute; left: 34px; width: 152px; top: 260px; height: 1.5px; background: var(--panel-text); }
  .title-strength { top: 276px; font-size: 21px; letter-spacing: 0.3px; }

  .ingredient-list {
    position: absolute; left: 56px; top: 457px; list-style: none;
    font-size: 15px; color: var(--ink); line-height: 25.7px;
  }
  .claim-rule { left: 28px; width: 130px; top: 586px; height: 2px; }
  .claim { position: absolute; left: 26px; top: 597px; font-size: 15px; color: var(--ink); }

  .brand {
    position: absolute; left: 146px; top: 620px; width: 110px; text-align: center;
  }
  .brand-dot {
    display: block; width: 30px; height: 30px; margin: 0 auto 6px;
    border: 2px solid var(--ink); border-radius: 50%;
  }
  .brand-name {
    font-family: "Cabin Condensed", sans-serif; font-size: 22px; font-weight: 500;
    color: var(--brand-blue); border-bottom: 1.5px solid var(--ink); padding: 0 2px;
  }

  .volume {
    position: absolute; left: 0; width: 100%; top: 704px; text-align: center;
    font-size: 15px; color: var(--ink); letter-spacing: 0.3px;
  }
  .base-band { left: 0; width: 100%; bottom: 0; height: 20px; }
</style>
</head>
<body>
  <main class="carton-front">
    <section class="title-panel">
      <div class="gold-rule top"></div>
      <div class="title-word title-vitamin">Vitamin</div>
      <div class="title-word title-letter">C</div>
      <div class="title-word title-serum">Serum</div>
      <div class="title-divider"></div>
      <div class="title-word title-strength">High Strength</div>
      <div class="gold-rule bottom"></div>
    </section>

    <ul class="ingredient-list">
      <li>Vitamin C</li>
      <li>Vitamin B3</li>
      <li>Vitamin B5</li>
      <li>Vitamin E</li>
      <li>Ferulic acid</li>
    </ul>
    <div class="gold-rule claim-rule"></div>
    <p class="claim">Treats pigmentation</p>

    <div class="brand">
      <span class="brand-dot"></span>
      <span class="brand-name">DermaLune</span>
    </div>

    <p class="volume">℮ 30 ml / 1 fl.oz.</p>
    <div class="gold-rule base-band"></div>
  </main>
</body>
</html>
```